ARC VOLLEY Business Card Project

I'd like to request a business card design for the new company I've launched.
The name of the company is "ARC VOLLEY" an indoor unmanned tennis practice facility.
We would like to see designs that use our brand identity color in the logo I've attached.
We hope to get the design with modern, luxurious and elegant tone and manner.
We hope the logo should not be too big.

Business card must have elements as below:
- Logo (One of the logos I've attached)
- Name (In Korean Text) : 박 서 윤
- Title (In Korean Text) : 대표
- Phone Number : 010-8472-3916
- Email Address : seoyun.park@arcvolley-example.co.kr
- Website : www.arcvolley-example.co.kr
- Instagram : arcvolley
- Address (In Korean text) : 경기도 용인시 수지구 풍덕천로 456 미래타워 5층 501호, 502호

Target Market(s)

Tennis amateurs in 20 to 40s

Industry/Entity Type

Sports, Hobby

Contact Information for Business Card

- Logo (One of the logos I've attached) - Name (In Korean Text) : 박 서 윤 - Title (In Korean Text) : 대표 - Phone Number : 010-8472-3916 - Email Address : seoyun.park@arcvolley-example.co.kr - Website : www.arcvolley-example.co.kr - Instagram : arcvolley - Address (In Korean text) : 경기도 용인시 수지구 풍덕천로 456 미래타워 5층 501호, 502호

Font styles to use
Sans Serif

Requirements
Must have
• Double sided
Nice to have
• Logo with intaglio or relief embossing
Should not have
• Logo should not be too big.

```html
<!DOCTYPE html>
<html lang="ko">
<head>
<meta charset="utf-8">
<title>ARC VOLLEY Business Card</title>
<link href="https://fonts.googleapis.com/css2?family=Lato:wght@400;700&family=Noto+Sans+KR:wght@300;400&display=swap" rel="stylesheet">
<style>
  :root {
    --brand-green: #2f5239;
    --paper: #ffffff;
    --backdrop: #1c1c1c;
    --divider: rgba(255,255,255,0.35);
  }
  * { margin: 0; padding: 0; box-sizing: border-box; }
  html, body { width: 1200px; height: 1015px; overflow: hidden; }
  body {
    background: var(--backdrop);
    font-family: "Lato", sans-serif;
    position: relative;
  }
  .card {
    position: absolute;
    left: 280px;
    width: 640px;
    height: 360px;
    box-shadow: 0 10px 30px rgba(0,0,0,0.5);
    overflow: hidden;
  }
  .card--front { top: 115px; background: var(--brand-green); }
  .card--back { top: 540px; background: var(--paper); }

  .brand {
    position: absolute;
    display: flex;
    align-items: center;
    gap: 14px;
  }
  .brand__dot { width: 40px; height: 40px; border-radius: 50%; }
  .brand__name {
    font-family: "Lato", sans-serif;
    font-weight: 700;
    font-size: 30px;
    letter-spacing: 2px;
  }
  .card--front .brand { left: 50%; top: 50%; transform: translate(-50%, -50%); }
  .card--front .brand__dot { background: var(--paper); }
  .card--front .brand__name { color: var(--paper); }

  .card--back .brand { left: 50%; top: 58px; transform: translateX(-50%); }
  .card--back .brand__dot { background: var(--brand-green); }
  .card--back .brand__name { color: var(--brand-green); }

  .info-band {
    position: absolute;
    left: 0; right: 0;
    top: 148px;
    height: 150px;
    background: var(--brand-green);
    color: var(--paper);
  }
  .person {
    position: absolute;
    left: 140px;
    top: 52px;
    display: flex;
    align-items: flex-end;
    gap: 8px;
    font-family: "Noto Sans KR", sans-serif;
  }
  .person__name { font-size: 30px; font-weight: 300; letter-spacing: 2px; line-height: 1; }
  .person__title { font-size: 15px; font-weight: 400; line-height: 1; }
  .info-divider {
    position: absolute;
    left: 318px;
    top: 24px;
    width: 1px;
    height: 102px;
    background: var(--divider);
  }
  .contact-list {
    position: absolute;
    left: 338px;
    top: 24px;
    list-style: none;
    font-size: 13px;
    line-height: 25.5px;
  }
  .contact-list li { display: flex; align-items: center; gap: 7px; white-space: nowrap; }
  .contact-list svg { width: 14px; height: 14px; flex: none; }

  .address {
    position: absolute;
    left: 0; right: 0;
    top: 298px;
    height: 62px;
    display: flex;
    align-items: center;
    justify-content: center;
    font-family: "Noto Sans KR", sans-serif;
    font-size: 13px;
    font-weight: 400;
    color: var(--brand-green);
    white-space: nowrap;
  }
</style>
</head>
<body>
  <section class="card card--front" aria-label="Card front">
    <div class="brand">
      <span class="brand__dot"></span>
      <span class="brand__name">ARC VOLLEY</span>
    </div>
  </section>

  <section class="card card--back" aria-label="Card back">
    <div class="brand">
      <span class="brand__dot"></span>
      <span class="brand__name">ARC VOLLEY</span>
    </div>
    <div class="info-band">
      <div class="person">
        <span class="person__name">박 서 윤</span>
        <span class="person__title">대표</span>
      </div>
      <span class="info-divider"></span>
      <ul class="contact-list">
        <li>
          <svg viewBox="0 0 16 16" aria-hidden="true"><circle cx="8" cy="8" r="8" fill="#fff"/><path d="M5 4.5l1.5-.5 1 2-1 .8a5 5 0 0 0 2.7 2.7l.8-1 2 1-.5 1.5c-3.5 0-6.5-3-6.5-6.5z" fill="#2f5239"/></svg>
          010-8472-3916
        </li>
        <li>
          <svg viewBox="0 0 16 16" aria-hidden="true"><rect x="1" y="3.5" width="14" height="9" fill="#fff"/><path d="M1 3.5l7 5 7-5" fill="none" stroke="#2f5239" stroke-width="1.2"/></svg>
          seoyun.park@arcvolley-example.co.kr
        </li>
        <li>
          <svg viewBox="0 0 16 16" aria-hidden="true"><circle cx="8" cy="8" r="7.5" fill="#fff"/><g fill="none" stroke="#2f5239" stroke-width="1"><ellipse cx="8" cy="8" rx="3" ry="7"/><path d="M1 8h14M2.5 4.5h11M2.5 11.5h11"/></g></svg>
          www.arcvolley-example.co.kr
        </li>
        <li>
          <svg viewBox="0 0 16 16" aria-hidden="true"><rect x="1.5" y="1.5" width="13" height="13" rx="2" fill="#fff"/></svg>
          @arcvolley
        </li>
      </ul>
    </div>
    <p class="address">경기도 용인시 수지구 풍덕천로 456 미래타워 5층 501호, 502호</p>
  </section>
</body>
</html>
```